A online shop for solid wood need a Stationary design

A new online shop (in Austria and Germany) for solid wood and steel furniture (feldberg-formwerk) needs a Stationay design (letterhead, business card, envelope etc...). Dining tables, coffee tables, TV furniture and similar furniture will be sold. Everything will be custom made.

```html
<!DOCTYPE html>
<html lang="en">
<head>
<meta charset="utf-8">
<title>Feldberg Formwerk – Stationery</title>
<link href="https://fonts.googleapis.com/css2?family=Hind:wght@400;500;600;700&display=swap" rel="stylesheet">
<style>
:root{
  --red:#d9161f;
  --grey-band:#9d9ea1;
  --paper:#f1f1f1;
  --bg:#dddddd;
  --ink:#1d1d1d;
  --muted:#8a8a8a;
  --window:#99999c;
}
*{margin:0;padding:0;box-sizing:border-box}
html,body{width:1200px;height:792px;overflow:hidden}
body{background:var(--bg);font-family:"Hind",sans-serif;color:var(--ink);position:relative}
.sheet{position:absolute;background:var(--paper);overflow:hidden}
.band{position:absolute;left:0;right:0;bottom:0;display:flex}
.band .grey{background:var(--grey-band)}
.band .mark{background:#fff}
.band .red{background:var(--red);flex:1}
.brand{color:var(--red);font-weight:700;line-height:1;letter-spacing:.06em;text-transform:uppercase}
.brand-square{display:block;background:var(--red)}
.red-text{color:var(--red)}
.contact{list-style:none;color:var(--muted)}
.contact li{display:flex;align-items:flex-start}
.contact svg{flex:none;fill:var(--red)}
.tagline{font-weight:600;line-height:1.25}

/* business card front */
.card-front{left:184px;top:132px;width:170px;height:97px}
.card-front .brand-square{position:absolute;left:10px;top:8px;width:14px;height:14px}
.card-front .brand{position:absolute;left:8px;top:27px;font-size:7.5px}
.card-front .holder{position:absolute;left:112px;top:35px;font-size:6.5px;font-weight:500;line-height:1.1}
.card-front .holder small{display:block;font-size:3.5px;color:var(--muted);font-weight:400}
.card-front .rule{position:absolute;left:8px;right:8px;top:50px;height:.6px;background:var(--red)}
.card-front .contact{position:absolute;left:8px;top:60px;font-size:3px;line-height:1.5}
.card-front .contact svg{width:3px;height:3px;margin:1px 3px 0 0}
.card-front .tagline{position:absolute;left:112px;top:60px;font-size:3px}
.card-front .desc{position:absolute;left:112px;top:69px;font-size:2.8px;color:var(--muted);line-height:1.3}
.card-front .band{height:6px}

/* business card back */
.card-back{left:379px;top:132px;width:170px;height:97px;background:var(--red);color:#fff;text-align:center}
.card-back .brand-square{position:absolute;left:78px;top:26px;width:14px;height:14px;background:#fff}
.card-back .brand{position:absolute;left:0;right:0;top:48px;color:#fff;font-size:11px}
.card-back .web{position:absolute;left:0;right:0;top:79px;font-size:4px;font-weight:500}

/* window envelope */
.env-front{left:184px;top:255px;width:365px;height:182px}
.env-front .brand-square{position:absolute;left:14px;top:12px;width:20px;height:20px}
.env-front .brand{position:absolute;left:11px;top:38px;font-size:9.5px}
.env-front .tagline{position:absolute;left:11px;top:62px;font-size:4.5px}
.env-front .contact{position:absolute;left:11px;top:78px;font-size:4.2px;line-height:1.65}
.env-front .contact svg{width:4.5px;height:4.5px;margin:.8px 5px 0 0}
.env-front .studio{position:absolute;left:260px;top:13px;font-size:5.8px;font-weight:500}
.env-front .studio-desc{position:absolute;left:260px;top:21px;font-size:3.6px;color:var(--muted);line-height:1.3}
.env-front .window{position:absolute;left:260px;top:122px;width:97px;height:38px;background:var(--window);border-radius:2px}
.env-front .band{height:11px}

/* envelope back */
.env-back{left:184px;top:468px;width:365px;height:182px}
.env-back .flap{position:absolute;left:0;top:0}
.env-back .brand-square{position:absolute;left:172px;top:8px;width:20px;height:20px}
.env-back .brand{position:absolute;left:0;right:0;top:35px;text-align:center;font-size:9.5px}
.env-back .band{height:12px}

/* letterhead */
.letter{left:595px;top:131px;width:367px;height:519px}
.letter .brand-square{position:absolute;left:22px;top:24px;width:40px;height:40px}
.letter .brand{position:absolute;left:15px;top:72px;font-size:15px}
.letter .tagline{position:absolute;left:245px;top:24px;font-size:6.8px}
.letter .contact{position:absolute;left:245px;top:47px;font-size:6.2px;line-height:1.6}
.letter .contact li{margin-bottom:1px}
.letter .contact svg{width:6px;height:6px;margin:1.3px 8px 0 0}
.letter .studio{position:absolute;left:15px;top:133px;font-size:9.5px;font-weight:500}
.letter .studio-desc{position:absolute;left:15px;top:148px;font-size:6.2px;color:var(--muted);line-height:1.25}
.letter .salutation{position:absolute;left:15px;top:180px;font-size:6px;font-weight:500}
.letter .salutation b{color:var(--red);font-weight:600;margin-left:3px}
.letter .body{position:absolute;left:15px;top:197px;width:337px;font-size:5px;line-height:1.3;color:var(--muted)}
.letter .body p{margin-bottom:6px}
.letter .signature{position:absolute;left:15px;top:337px;width:62px;height:16px;background:linear-gradient(90deg,rgba(217,22,31,.18),rgba(217,22,31,.06))}
.letter .sig-rule{position:absolute;left:15px;top:354px;width:62px;height:.8px;background:var(--red)}
.letter .closing{position:absolute;left:15px;top:358px;font-size:6px;font-weight:500}
.letter .band{height:15px}
</style>
</head>
<body>

<svg width="0" height="0" style="position:absolute">
  <symbol id="i-pin" viewBox="0 0 10 10"><path d="M5 0a3.6 3.6 0 0 0-3.6 3.6C1.4 6.3 5 10 5 10s3.6-3.7 3.6-6.4A3.6 3.6 0 0 0 5 0zm0 5a1.4 1.4 0 1 1 0-2.8A1.4 1.4 0 0 1 5 5z"/></symbol>
  <symbol id="i-phone" viewBox="0 0 10 10"><path d="M2 .5l1.8 2.2-1 1.2a6 6 0 0 0 3.3 3.3l1.2-1L9.5 8 8.3 9.5C4.4 9.3.7 5.6.5 1.7z"/></symbol>
  <symbol id="i-mail" viewBox="0 0 10 10"><path d="M0 2h10v6H0zm.8.6L5 5.6l4.2-3z" fill-rule="evenodd"/></symbol>
  <symbol id="i-web" viewBox="0 0 10 10"><path d="M5 0a5 5 0 1 0 0 10A5 5 0 0 0 5 0zm0 1c.7.8 1.1 2 1.2 3.5H3.8C3.9 3 4.3 1.8 5 1zM1 5.5h1.8c.1 1.3.4 2.4.9 3.2A4 4 0 0 1 1 5.5zm0-1a4 4 0 0 1 2.7-3.2c-.5.8-.8 1.9-.9 3.2zm4 4.5c-.7-.8-1.1-2-1.2-3.5h2.4C6.1 7 5.7 8.2 5 9zm1.3-.3c.5-.8.8-1.9.9-3.2H9a4 4 0 0 1-2.7 3.2zM7.2 4.5c-.1-1.3-.4-2.4-.9-3.2A4 4 0 0 1 9 4.5z"/></symbol>
</svg>

<!-- business card, front -->
<section class="sheet card-front">
  <span class="brand-square"></span>
  <div class="brand">Feldberg<br>Formwerk</div>
  <div class="holder">LENA <span class="red-text">MARBACH</span><small>furniture maker</small></div>
  <div class="rule"></div>
  <ul class="contact">
    <li><svg><use href="#i-pin"/></svg>your address here, state, zip code 0004</li>
    <li><svg><use href="#i-phone"/></svg>+43 1 555 01 42</li>
    <li><svg><use href="#i-mail"/></svg>info@feldberg-formwerk.at</li>
    <li><svg><use href="#i-web"/></svg>www.feldberg-formwerk.at</li>
  </ul>
  <div class="tagline">Online furniture in <span class="red-text">solid timber</span><br>and <span class="red-text">blackened steel</span></div>
  <div class="desc">Tables, sideboards and<br>media units, each one<br>built to your measurements.</div>
  <div class="band"><span class="grey" style="width:113px"></span><span class="mark" style="width:8px"></span><span class="red"></span></div>
</section>

<!-- business card, back -->
<section class="sheet card-back">
  <span class="brand-square"></span>
  <div class="brand">Feldberg Formwerk</div>
  <div class="web">www.feldberg-formwerk.at</div>
</section>

<!-- window envelope -->
<section class="sheet env-front">
  <span class="brand-square"></span>
  <div class="brand">Feldberg<br>Formwerk</div>
  <div class="tagline">Online furniture in<br><span class="red-text">solid timber</span> and <span class="red-text">blackened steel</span></div>
  <ul class="contact">
    <li><svg><use href="#i-pin"/></svg>your address here, state,<br>zip code 0004</li>
    <li><svg><use href="#i-phone"/></svg>+43 1 555 01 42</li>
    <li><svg><use href="#i-mail"/></svg>hallo@feldberg-formwerk.at</li>
    <li><svg><use href="#i-web"/></svg>www.feldberg-formwerk.at</li>
  </ul>
  <div class="studio">BUILT TO <span class="red-text">MEASURE</span></div>
  <div class="studio-desc">Tables, sideboards and media units,<br>each one built to your measurements.</div>
  <div class="window"></div>
  <div class="band"><span class="grey" style="width:262px"></span><span class="mark" style="width:17px"></span><span class="red"></span></div>
</section>

<!-- envelope, back -->
<section class="sheet env-back">
  <svg class="flap" width="365" height="60"><polyline points="0,0 23,56 342,56 365,0" fill="none" stroke="#cfcfcf" stroke-width=".8"/></svg>
  <span class="brand-square"></span>
  <div class="brand">Feldberg<br>Formwerk</div>
  <div class="band"><span class="grey" style="width:265px"></span><span class="mark" style="width:19px"></span><span class="red"></span></div>
</section>

<!-- letterhead -->
<section class="sheet letter">
  <span class="brand-square"></span>
  <div class="brand">Feldberg<br>Formwerk</div>
  <div class="tagline">Online furniture in <span class="red-text">solid timber</span><br>and <span class="red-text">blackened steel</span></div>
  <ul class="contact">
    <li><svg><use href="#i-pin"/></svg>your address here, state,<br>zip code 0004</li>
    <li><svg><use href="#i-phone"/></svg>+43 1 555 01 42</li>
    <li><svg><use href="#i-mail"/></svg>hallo@feldberg-formwerk.at</li>
    <li><svg><use href="#i-web"/></svg>www.feldberg-formwerk.at</li>
  </ul>
  <div class="studio">BUILT TO <span class="red-text">MEASURE</span></div>
  <div class="studio-desc">Tables, sideboards and<br>media units, each one<br>built to your measurements.</div>
  <div class="salutation">Dear<b>Lena Marbach</b></div>
  <div class="body">
    <p>Thank you for your interest in our furniture. Every piece we make starts with a conversation about your room, your habits and the way you like to live. From that first sketch we choose the timber, shape the steel frame and finish each surface by hand in our workshop, so that the table or cabinet you receive fits your home exactly and will last for many years to come.</p>
    <p>Our range covers dining tables, coffee tables, sideboards and media units. Each model can be adjusted in size, wood species, oil finish and frame colour to suit your wishes.</p>
    <p>Once you have placed your order, we send you a detailed drawing and a fixed delivery date. Our team keeps you informed at every step and delivers across Austria and Germany. If you have any questions about materials, care or measurements, simply reply to this letter or call us directly, we are always glad to help.</p>
  </div>
  <div class="signature" role="img" aria-label="Handwritten signature of Jonas Reiter in red ink"></div>
  <div class="sig-rule"></div>
  <div class="closing">Sincerely</div>
  <div class="band"><span class="grey" style="width:243px"></span><span class="mark" style="width:25px"></span><span class="red"></span></div>
</section>

</body>
</html>
```